New Business Cards for Torvin Group

We need a new Business Card to compliment our new logo. We are a vibrant design, manufacture and install business providing recreation areas, public parks and Municipal spaces. We want business cards that are classy, modern and clean.

We have recently changed our logo, and are celebrating our 40th anniversary. We want business cards with a new modern design to reflect our status.

Target Market(s)

Customers

Contact Information for Business Card

We need all the details of our 3 offices as per the business card attached. Please disregard the old logo on the business card, the other three files show our new logo.

Requirements
Must have
• All info as per attached business card but with new logo.
Nice to have

```html
<!DOCTYPE html>
<html lang="en">
<head>
<meta charset="utf-8">
<title>Torvin Group – Business Card</title>
<link rel="stylesheet" href="https://fonts.googleapis.com/css2?family=Montserrat:wght@500;600;700&family=Open+Sans:wght@400&display=swap">
<style>
  :root {
    --stage: #5e5e5e;
    --card: #ffffff;
    --brand-red: #e8323a;
    --brand-red-dark: #a3161c;
    --ink: #3a3a3a;
    --ink-soft: #5c5c5c;
    --rule: #8a8a8a;
  }
  * { box-sizing: border-box; margin: 0; padding: 0; }
  html, body {
    width: 1200px; height: 1200px; overflow: hidden;
    background: var(--stage);
  }
  .card {
    position: absolute;
    left: 137px; top: 335px;
    width: 926px; height: 530px;
    background: var(--card);
    border-radius: 30px;
    overflow: hidden;
    font-family: "Open Sans", Arial, sans-serif;
    color: var(--ink);
  }
  .card__tab {
    position: absolute; left: 0; top: 102px;
    width: 11px; height: 64px;
    background: var(--brand-red);
    border-radius: 0 4px 4px 0;
  }
  .holder__name {
    position: absolute; left: 31px; top: 100px;
    font-family: "Montserrat", Arial, sans-serif;
    font-weight: 700; font-size: 26px;
    color: var(--brand-red); line-height: 1.2;
  }
  .holder__title {
    position: absolute; left: 31px; top: 138px;
    font-size: 24px; color: var(--ink); line-height: 1.2;
  }
  .holder__contact {
    position: absolute; left: 31px; top: 223px;
    font-size: 19px; color: var(--ink-soft); line-height: 38px;
    list-style: none;
  }
  .holder__contact b { font-weight: 400; color: var(--ink); }
  .brand {
    position: absolute; right: 40px; top: 68px;
    display: flex; align-items: center; gap: 14px;
  }
  .brand__dot {
    width: 92px; height: 92px; border-radius: 50%;
    background: var(--brand-red);
  }
  .brand__name {
    font-family: "Montserrat", Arial, sans-serif;
    font-weight: 700; font-size: 34px;
    color: var(--brand-red); line-height: 1;
  }
  .card__rule {
    position: absolute; left: 31px; top: 303px;
    width: 855px; height: 2px; background: var(--rule);
  }
  .office {
    position: absolute; top: 322px;
    font-size: 15.5px; color: var(--ink-soft); line-height: 28px;
  }
  .office--head { left: 31px; }
  .office--dubai { left: 355px; }
  .office--qatar { left: 652px; top: 326px; }
  .office__heading {
    font-family: "Montserrat", Arial, sans-serif;
    font-weight: 600; font-size: 20px;
    color: var(--brand-red); line-height: 28px;
    margin-bottom: 6px;
  }
  .office__lines { list-style: none; }
  .ribbon {
    position: absolute; left: 230px; top: 487px;
    width: 476px; height: 43px;
  }
  .ribbon__url {
    position: absolute; left: 230px; top: 487px;
    width: 476px; height: 43px;
    display: flex; align-items: center; justify-content: center;
    font-size: 19px; color: #ffffff;
  }
</style>
</head>
<body>
  <article class="card">
    <span class="card__tab"></span>

    <h1 class="holder__name">Karim Nasrallo</h1>
    <p class="holder__title">Managing Partner</p>
    <ul class="holder__contact">
      <li><b>Phone:</b> +971 (0)50 555 0148</li>
      <li><b>Email:</b> karim@torvingroup.com</li>
    </ul>

    <div class="brand">
      <span class="brand__dot"></span>
      <span class="brand__name">Torvin Group</span>
    </div>

    <span class="card__rule"></span>

    <section class="office office--head">
      <h2 class="office__heading">Head Office</h2>
      <ul class="office__lines">
        <li>P.O. Box: 10482 Abu Dhabi. U.A.E</li>
        <li>Tel No: +971 (0)2 5550174</li>
        <li>Fax No: +971(0)2 5550175</li>
        <li>Email: sales@torvingroup.com</li>
      </ul>
    </section>

    <section class="office office--dubai">
      <h2 class="office__heading">Dubai Office</h2>
      <ul class="office__lines">
        <li>P.O. Box: 208813 Dubai, U.A.E</li>
        <li>Tel No: +971 (0)4 555021</li>
        <li>Fax No: +971(0)4 555022</li>
        <li>Email: sales@torvingroup.com</li>
      </ul>
    </section>

    <section class="office office--qatar">
      <h2 class="office__heading">Qater Office</h2>
      <ul class="office__lines">
        <li>P.O. Box: 30527 Doha, Qatter</li>
        <li>Tel No: +974 55500316</li>
        <li>Fax No: +971 55500317</li>
        <li>Email: sales@torvingroup.com</li>
      </ul>
    </section>

    <svg class="ribbon" viewBox="0 0 476 43" aria-hidden="true">
      <polygon points="5,26 24,0 30,26" fill="var(--brand-red-dark)"/>
      <polygon points="471,26 452,0 446,26" fill="var(--brand-red-dark)"/>
      <polygon points="24,0 452,0 440,43 36,43" fill="var(--brand-red)"/>
    </svg>
    <p class="ribbon__url">www.torvingroup.com</p>
  </article>
</body>
</html>
```